Homepage für Immobilienmakler
Zielgruppe
Wir sind ein neuer und junger Immobilienmakler. Wir wollen moderne und neue Wege gehen. Damit meinen wir, extrem modern und auffallend professionell.
Unsere Immobilien sind von Anlegerwohnungen über Häuser bis hin zu Gewerbeimmobilien
Unsere Zielgruppe ist von jung bis alt quer durch.
Aufgabenstellung
Homepagegestalltung für unsere Immobilienmaklerei.
Persönlich gefällt mir sehr gut das schwarz-weiß, jedoch wirkt das dann eher zu dunkel nehme ich mal an. Sonst würde mir die Homepage in grün, wie die Farbe im Logo, gut gefallen. Eventuell in weißer Schrift. ABER, ICH ÜBERLASSE EUCH DIE DESIGNSFARBEN.
Mir hätte dieses Design sehr gut gefallen, eventuelll könnt ihr dieses umgestallten:
http://vorlagenhain.example/item/auto-dealer-car-dealer-html-template/full_screen_preview/7719034
Kein muss, wenn ihr etwas besseres habt, dann bin ich auch froh ;)
Eventuell etwas mit Bewegung auf der Homepage oder so wäre auch gut.
Unsere Homepage hat die Domain:
wohnraum-kontor.example
Das Foto von mir sollte auf der Homepage eingebaut werden.
Auf der Homepage sollen die Immobilien, die wir verkaufen und vermieten angeführt werden. Zudem sollte ersichtlich sein, dass wir Immobilien suchen, um diese zu verkaufen oder zu vermieten.

```html
<!DOCTYPE html>
<html lang="en">
<head>
<meta charset="utf-8">
<title>Wohnraum Kontor – Real Estate</title>
<link href="https://fonts.googleapis.com/css2?family=Roboto:wght@300;400;500;700&family=Roboto+Condensed:wght@700&display=swap" rel="stylesheet">
<style>
:root{
  --green:#45b649;
  --green-light:#6fd072;
  --green-tab:#dcebdc;
  --ink:#111;
  --text:#333;
  --muted:#888;
  --page-bg:#e6e6e6;
  --band:#f1f1f1;
  --line:#ddd;
  --white:#fff;
}
*{margin:0;padding:0;box-sizing:border-box}
html,body{width:889px;height:1200px;overflow:hidden}
body{background:var(--page-bg);font-family:"Roboto",sans-serif;color:var(--text);position:relative}
.abs{position:absolute}
.topbar{left:0;top:0;width:889px;height:26px;background:#efefef}
.topbar .contact{top:7px;font-size:10px;color:#999;font-weight:300}
.page{left:21px;top:26px;width:848px;height:1103px;background:var(--white);box-shadow:0 0 3px rgba(0,0,0,.08)}
.logo{font-family:"Roboto Condensed",sans-serif;font-weight:700;font-size:31px;color:var(--green);letter-spacing:-.5px;display:flex;align-items:center;gap:6px;white-space:nowrap}
.logo .dot{width:10px;height:10px;border-radius:50%;background:var(--ink)}
.nav a{position:absolute;top:0;font-size:12px;color:var(--ink);text-decoration:none;font-weight:400;white-space:nowrap}
.nav .active::before{content:"";position:absolute;left:0;right:0;top:-10px;height:2px;background:var(--green)}
.hero{left:0;top:64px;width:848px;height:299px;background:linear-gradient(180deg,#6d8a50 0%,#4d7030 40%,#7aa04a 62%,#3f6a24 100%)}
.search{left:582px;top:98px;width:245px;height:282px;background:var(--green);border:2px solid var(--green-light);box-shadow:0 8px 8px -6px rgba(0,0,0,.25)}
.search h3{position:absolute;left:0;right:0;top:10px;text-align:center;color:var(--white);font-weight:500;font-size:14px}
.field{position:absolute;height:22px;background:var(--white);font-size:10px;color:#999;padding:5px 6px;font-weight:300}
.field::after{content:"";position:absolute;right:8px;top:8px;border-left:4px solid transparent;border-right:4px solid transparent;border-top:6px solid var(--ink)}
.btn-search{position:absolute;left:17px;top:229px;width:210px;height:24px;background:#1b1d20;color:var(--white);font-size:13px;font-weight:500;text-align:center;line-height:24px}
.intro{left:19px;top:401px;width:808px;height:106px;background:#000}
.intro .portrait{position:absolute;left:29px;top:10px;width:68px;height:96px;background:linear-gradient(180deg,#5a4a3e,#d8d8d8 60%,#eee)}
.intro h2{position:absolute;left:136px;top:19px;color:var(--white);font-size:20px;font-weight:500}
.intro p{position:absolute;left:136px;top:45px;width:662px;color:#ccc;font-size:9.6px;line-height:16.2px;font-weight:300;text-align:justify}
.listings{left:0;top:539px;width:848px;height:217px;background:var(--band)}
.tab{position:absolute;top:18px;height:27px;font-size:11.5px;font-weight:500;line-height:27px;padding:0 10px;white-space:nowrap}
.tab.on{left:19px;background:var(--green-tab);color:var(--green)}
.tab.off{left:200px;color:var(--ink)}
.arrow{position:absolute;top:100px;font-size:24px;color:#bbb;font-weight:300}
.card{position:absolute;top:60px;width:184px;height:131px;background:var(--white);border:1px solid #e0e0e0}
.card .img{position:absolute;left:4px;top:4px;width:175px;height:98px}
.card .cap{position:absolute;left:8px;top:110px;font-size:9.5px;color:var(--ink);white-space:nowrap}
.card .price{position:absolute;right:10px;top:107px;font-size:12px;color:var(--green);white-space:nowrap}
.col h2{position:absolute;top:0;font-size:19px;font-weight:400;color:var(--ink);white-space:nowrap}
.news{position:absolute;width:280px;height:60px}
.news .thumb{position:absolute;left:0;top:0;width:78px;height:57px;background:linear-gradient(135deg,#6da0d8,#f0c8a8 55%,#b48a4a)}
.news .t{position:absolute;left:85px;top:0;font-size:9.7px;color:var(--ink);white-space:nowrap}
.news .d{position:absolute;left:85px;top:15px;font-size:9.5px;color:var(--muted);line-height:14.5px;font-weight:300;white-space:nowrap}
.news .more{position:absolute;left:86px;top:45px;font-size:9.5px;color:var(--green);font-style:italic;font-weight:300}
.offer{position:absolute;font-size:9.7px;color:var(--ink);display:flex;align-items:center;gap:10px;white-space:nowrap}
.offer svg{width:14px;height:14px}
.agent{position:absolute;width:208px;height:92px;background:#f8f8f8;border:1px solid #eee}
.agent .ph{position:absolute;left:9px;top:8px;width:66px;height:76px;background:linear-gradient(180deg,#caa58a,#7e6550 55%,#141414 70%)}
.agent .n{position:absolute;left:80px;top:12px;font-size:9.5px;color:var(--ink)}
.agent .d{position:absolute;left:80px;top:27px;width:122px;font-size:9.5px;color:var(--muted);line-height:14.5px;font-weight:300}
.more-btn{position:absolute;top:1055px;width:57px;height:26px;background:#f2f2f2;border-bottom:2px solid #ddd;font-size:10.5px;color:var(--ink);text-align:center;line-height:26px}
.footer-brand{left:23px;top:1148px;display:flex;align-items:flex-end;gap:8px}
.footer-brand .logo{font-size:26px}
.foot-copy{font-size:9.5px;color:var(--ink);padding-bottom:6px;white-space:nowrap}
.foot-links{right:22px;top:1165px;font-size:9.5px;color:var(--ink);word-spacing:2px;white-space:nowrap}
</style>
</head>
<body>
<div class="abs topbar">
  <span class="abs contact" style="left:40px">&#9990; +1 800 5550 300</span>
  <span class="abs contact" style="left:155px">&#9993; info@wohnraum-kontor.example</span>
</div>

<div class="abs page">
  <div class="abs logo" style="left:18px;top:12px">Wohnraum Kontor <span class="dot"></span></div>
  <nav class="abs nav" style="left:0;top:41px;width:848px">
    <a class="active" style="left:338px">HOME</a>
    <a style="left:406px">ABOUT US</a>
    <a style="left:493px">RESALE PROPERTIES</a>
    <a style="left:638px">BUY PROPERTIES</a>
    <a style="left:765px">CONTACTS</a>
  </nav>

  <div class="abs hero" role="img" aria-label="Photo of a stone family house on a green lawn surrounded by trees"></div>

  <form class="abs search">
    <h3>SEARCH FOR PROPERTIES</h3>
    <div class="field" style="left:17px;top:40px;width:210px">Select Location</div>
    <div class="field" style="left:17px;top:78px;width:210px">Property type</div>
    <div class="field" style="left:17px;top:116px;width:210px">Property for sale</div>
    <div class="field" style="left:17px;top:154px;width:100px">Min bedrooms</div>
    <div class="field" style="left:127px;top:154px;width:100px">Price range</div>
    <div class="field" style="left:17px;top:191px;width:100px">Availability</div>
    <div class="field" style="left:127px;top:191px;width:100px">Furnished</div>
    <div class="btn-search">SEARCH</div>
  </form>

  <section class="abs intro">
    <div class="portrait" role="img" aria-label="Portrait of the agency founder in a white polo shirt"></div>
    <h2>WE KNOW WHAT YOU WANT</h2>
    <p>Lorem ipsum dolor sit amet, consectetur adipiscing elit. Mauris et ultricies odio, vitae tincidunt ante. In eu mi risus. Integer ante elit, rhoncus et dapibus dignissim, blandit a dolor. Sed luctus odio quis velit aliquet luctus. In felis nulla, aliquet a feugiat mattis, suscipit sed velit. Quisque adipiscing orci ac arcu ultrices rutrum. Pellentesque sit amet pharetra risus, vel malesuada diam. Aenean tristique mauris id euismod nulla.</p>
  </section>

  <section class="abs listings">
    <div class="tab on">REAL ESTATE FOR SALE</div>
    <div class="tab off">REAL ESTATE FOR RENT</div>
    <span class="arrow" style="left:23px">&#10094;</span>
    <span class="arrow" style="left:815px">&#10095;</span>
    <div class="card" style="left:41px"><div class="img" role="img" aria-label="White villa with palm trees" style="background:linear-gradient(180deg,#8ab8e8,#e8e8e8 50%,#5f8a3e)"></div><span class="cap">Lorem ipsum dolor sit</span><span class="price">&euro; 139,000</span></div>
    <div class="card" style="left:235px"><div class="img" role="img" aria-label="Brick family house" style="background:linear-gradient(180deg,#9cc4ea,#9a6a50 50%,#6a7a4a)"></div><span class="cap">Lorem ipsum dolor sit</span><span class="price">&euro; 139,000</span></div>
    <div class="card" style="left:429px"><div class="img" role="img" aria-label="Two-storey house among trees" style="background:linear-gradient(180deg,#6a9a4a,#d8d8c8 50%,#4a7a2a)"></div><span class="cap">Lorem ipsum dolor sit</span><span class="price">&euro; 139,000</span></div>
    <div class="card" style="left:622px"><div class="img" role="img" aria-label="Large stone manor" style="background:linear-gradient(180deg,#9cbad8,#a89880 50%,#7a8a5a)"></div><span class="cap">Lorem ipsum dolor sit</span><span class="price">&euro; 139,000</span></div>
  </section>

  <section class="abs col" style="left:19px;top:780px;width:300px;height:40px"><h2>WHAT’S NEW?</h2></section>
  <div class="news" style="left:19px;top:819px"><div class="thumb" role="img" aria-label="Hand holding a house key"></div><span class="t">Lorem ipsum dolor sit amet, consectetur</span><span class="d">Lorem ipsum dolor sit amet, consec-<br>tetur adipiscing elit. Mauris et ultricies</span><span class="more">Read more..&gt;&gt;</span></div>
  <div class="news" style="left:19px;top:898px"><div class="thumb" role="img" aria-label="Hand holding a house key"></div><span class="t">Lorem ipsum dolor sit amet, consectetur</span><span class="d">Lorem ipsum dolor sit amet, consec-<br>tetur adipiscing elit. Mauris et ultricies</span><span class="more">Read more..&gt;&gt;</span></div>
  <div class="news" style="left:19px;top:977px"><div class="thumb" role="img" aria-label="Hand holding a house key"></div><span class="t">Lorem ipsum dolor sit amet, consectetur</span><span class="d">Lorem ipsum dolor sit amet, consec-<br>tetur adipiscing elit. Mauris et ultricies</span><span class="more">Read more..&gt;&gt;</span></div>

  <section class="abs col" style="left:360px;top:780px;width:260px;height:40px"><h2>WHAT WE OFFER?</h2></section>
  <div class="offer" style="left:361px;top:823px"><svg viewBox="0 0 14 14"><circle cx="7" cy="7" r="7" fill="#e8e8e8"/><path d="M6 4l3 3-3 3" stroke="#45b649" stroke-width="1.8" fill="none"/></svg>Lorem ipsum dolor sit amet, consectetur</div>
  <div class="offer" style="left:361px;top:862px"><svg viewBox="0 0 14 14"><circle cx="7" cy="7" r="7" fill="#e8e8e8"/><path d="M6 4l3 3-3 3" stroke="#45b649" stroke-width="1.8" fill="none"/></svg>Lorem ipsum dolor sit amet, consectetur</div>
  <div class="offer" style="left:361px;top:901px"><svg viewBox="0 0 14 14"><circle cx="7" cy="7" r="7" fill="#e8e8e8"/><path d="M6 4l3 3-3 3" stroke="#45b649" stroke-width="1.8" fill="none"/></svg>Lorem ipsum dolor sit amet, consectetur</div>
  <div class="offer" style="left:361px;top:940px"><svg viewBox="0 0 14 14"><circle cx="7" cy="7" r="7" fill="#e8e8e8"/><path d="M6 4l3 3-3 3" stroke="#45b649" stroke-width="1.8" fill="none"/></svg>Lorem ipsum dolor sit amet, consectetur</div>
  <div class="offer" style="left:361px;top:979px"><svg viewBox="0 0 14 14"><circle cx="7" cy="7" r="7" fill="#e8e8e8"/><path d="M6 4l3 3-3 3" stroke="#45b649" stroke-width="1.8" fill="none"/></svg>Lorem ipsum dolor sit amet, consectetur</div>
  <div class="offer" style="left:361px;top:1018px"><svg viewBox="0 0 14 14"><circle cx="7" cy="7" r="7" fill="#e8e8e8"/><path d="M6 4l3 3-3 3" stroke="#45b649" stroke-width="1.8" fill="none"/></svg>Lorem ipsum dolor sit amet, consectetur</div>

  <section class="abs col" style="left:618px;top:780px;width:220px;height:40px"><h2>FIND YOUR AGENT.</h2></section>
  <div class="agent" style="left:619px;top:819px"><div class="ph" role="img" aria-label="Agent portrait"></div><span class="n">MEYER. K</span><span class="d">Lorem ipsum dolor sit amet, consectetur adipis ing elit. Mauris et ultricies</span></div>
  <div class="agent" style="left:619px;top:940px"><div class="ph" role="img" aria-label="Agent portrait"></div><span class="n">MEYER. K</span><span class="d">Lorem ipsum dolor sit amet, consectetur adipis ing elit. Mauris et ultricies</span></div>

  <div class="more-btn" style="left:19px">MORE</div>
  <div class="more-btn" style="left:360px">MORE</div>
  <div class="more-btn" style="left:619px">MORE</div>
</div>

<div class="abs footer-brand">
  <div class="logo">Wohnraum Kontor <span class="dot"></span></div>
  <div class="foot-copy">© 2013 | PRIVACY POLICY</div>
</div>
<div class="abs foot-links">HOME &nbsp;/&nbsp; ABOUT US &nbsp;/&nbsp; TERM &amp; CONDITIONS &nbsp;/&nbsp; IMPRINT &nbsp;/&nbsp; CONTACTS</div>
</body>
</html>
```